Modern card design needed for building development company

We are looking for a sharp modern new look for our business cards.
We are a New Zealand based company called TKR Ventures NZ LTD that specialises in subdividing large sections, housing and commercial buildings.
We have attached a photo of the current logo and would like to see it improved somehow as it looks a bit dated.
We are open to any colours.

Target Market(s)

Investors, Property buyers

Industry/Entity Type

Investment

Contact Information for Business Card

TKR VENTURES NZ LTD
www.tkrventuresnz.example.nz

Dorian Fletcher
Phone +64 21 843 209
Email dpfletcher@mailvane.example.nz

Font styles to use
Serif
Sans Serif

Colors
0792cd
33a6d7
85cae6
6b449b
886aae
f04a50
ec1f27
f37122
f68d4d

Requirements
Must have
• Please try and make the logo more modern or if you have a similar one we would like to see it.

```html
<!DOCTYPE html>
<html lang="en">
<head>
<meta charset="utf-8">
<title>TKR Ventures NZ LTD – Business Card</title>
<link rel="stylesheet" href="https://fonts.googleapis.com/css2?family=Montserrat:wght@700;800&family=Open+Sans:wght@400;600&display=swap">
<style>
  :root {
    --canvas: #ecebef;
    --card-white: #ffffff;
    --purple: #6b449b;
    --purple-dark: #52307f;
    --purple-soft: #c1b2d9;
    --ink: #3a3346;
    --white: #ffffff;
  }
  * { box-sizing: border-box; margin: 0; padding: 0; }
  html, body {
    width: 1200px; height: 1200px; overflow: hidden;
    background: var(--canvas);
  }
  .sheet {
    width: 1200px; height: 1200px;
    display: flex; flex-direction: column; align-items: center; justify-content: center;
    gap: 60px;
  }
  .card {
    position: relative;
    width: 760px; height: 434px;
    border-radius: 34px;
    overflow: hidden;
    box-shadow: 0 14px 30px rgba(40, 20, 70, 0.18);
  }
  .card-front { background: var(--card-white); }
  .card-back {
    background: linear-gradient(100deg, var(--purple-dark) 0%, var(--purple) 100%);
  }

  .company-name {
    font-family: "Montserrat", sans-serif;
    font-weight: 700;
    letter-spacing: 0.02em;
    white-space: nowrap;
  }
  .front-brand {
    position: absolute; left: 56px; top: 96px;
    display: flex; align-items: center; gap: 12px;
  }
  .front-brand .company-name { color: var(--purple); font-size: 28px; }
  .brand-square { width: 20px; height: 20px; background: var(--purple); flex: none; }

  .decor-block {
    position: absolute; right: 40px; top: 70px;
    width: 190px; height: 190px;
    background: var(--purple-soft);
  }

  .person-name {
    position: absolute; left: 56px; top: 232px;
    font-family: "Montserrat", sans-serif; font-weight: 800;
    font-size: 30px; color: var(--purple); letter-spacing: 0.01em;
    white-space: nowrap;
  }
  .contact-list {
    position: absolute; left: 56px; top: 290px;
    list-style: none;
    font-family: "Open Sans", sans-serif; font-size: 19px; color: var(--ink);
  }
  .contact-list li {
    display: flex; align-items: center; gap: 12px;
    height: 30px; white-space: nowrap;
  }
  .contact-icon { width: 20px; height: 20px; flex: none; }

  .back-brand {
    position: absolute; left: 50%; top: 50%;
    transform: translate(-50%, -50%);
    display: flex; align-items: center; gap: 16px;
  }
  .back-brand .company-name { color: var(--white); font-size: 38px; }
  .back-brand .brand-square { background: var(--white); width: 26px; height: 26px; }
</style>
</head>
<body>
<main class="sheet">
  <section class="card card-front" aria-label="Business card front">
    <div class="front-brand">
      <span class="brand-square"></span>
      <span class="company-name">TKR VENTURES NZ LTD</span>
    </div>
    <div class="decor-block" aria-hidden="true"></div>
    <h1 class="person-name">DORIAN FLETCHER</h1>
    <ul class="contact-list">
      <li>
        <svg class="contact-icon" viewBox="0 0 20 20" aria-hidden="true">
          <circle cx="10" cy="10" r="10" fill="var(--purple)"/>
          <path d="M6.5 5.5l2 0 .8 2.3-1.2 1c.6 1.2 1.5 2.1 2.7 2.7l1-1.2 2.3.8 0 2c0 .5-.4.9-.9.9C9 14 6 11 5.6 6.4c0-.5.4-.9.9-.9z" fill="var(--white)"/>
        </svg>
        +64 21 843 209
      </li>
      <li>
        <svg class="contact-icon" viewBox="0 0 20 20" aria-hidden="true">
          <circle cx="10" cy="10" r="10" fill="var(--purple)"/>
          <rect x="5" y="6.5" width="10" height="7" rx="1" fill="var(--white)"/>
          <path d="M5.3 7l4.7 3.5L14.7 7" fill="none" stroke="var(--purple)" stroke-width="1"/>
        </svg>
        dpfletcher@mailvane.example.nz
      </li>
      <li>
        <svg class="contact-icon" viewBox="0 0 20 20" aria-hidden="true">
          <circle cx="10" cy="10" r="10" fill="var(--purple)"/>
          <g fill="none" stroke="var(--white)" stroke-width="1.1">
            <circle cx="10" cy="10" r="5"/>
            <ellipse cx="10" cy="10" rx="2.2" ry="5"/>
            <path d="M5 10h10"/>
          </g>
        </svg>
        www.tkrventuresnz.example.nz
      </li>
    </ul>
  </section>

  <section class="card card-back" aria-label="Business card back">
    <div class="back-brand">
      <span class="brand-square"></span>
      <span class="company-name">TKR VENTURES NZ LTD</span>
    </div>
  </section>
</main>
</body>
</html>
```